New Business Card Design

We would like to refresh our business cards and make them look better. We are an IT company specialising in Cloud Services, IT Managed Services, software and hardware. I have attached a PSD of our current design. Also attached our logo.
Updates

I have uploaded all new logos in EPS format.

Can you please edit all designs to include a job title for Marcus Hale, eg. General Manager

Industry/Entity Type

Software

Colors
ffffff

Requirements
Must have
• Please use white background.
Should not have
• Black background

```html
<!DOCTYPE html>
<html lang="en">
<head>
<meta charset="utf-8">
<title>Clearpath Technology – Business Card</title>
<link rel="stylesheet" href="https://fonts.googleapis.com/css2?family=Jost:wght@400;500;600&family=Lato:wght@400&display=swap">
<style>
  :root{
    --canvas:#c9cfd7;
    --white:#ffffff;
    --ink:#1b1f24;
    --brand-red:#c0392b;
    --tagline:#7a8896;
    --blue-light:#86bde0;
    --blue-mid:#4f9bd0;
    --blue-deep:#2f7fb8;
    --text-body:#2a2e33;
  }
  html,body{margin:0;padding:0;}
  body{
    width:1004px;height:1200px;overflow:hidden;
    background:var(--canvas);
    position:relative;
    font-family:"Lato",Arial,sans-serif;
  }
  .card{
    position:absolute;left:69px;width:869px;
    background:var(--white);overflow:hidden;
    box-shadow:0 2px 6px rgba(0,0,0,.15);
  }
  .card--front{top:75px;height:483px;}
  .card--back{top:652px;height:478px;}
  .card__backdrop{position:absolute;inset:0;width:100%;height:100%;}

  .brand__name{
    position:absolute;margin:0;
    font-family:"Jost",Arial,sans-serif;font-weight:500;color:var(--ink);
    line-height:1;white-space:nowrap;letter-spacing:.02em;
  }
  .card--front .brand__name{left:33px;top:290px;font-size:34px;}
  .card--back .brand__name{left:420px;top:102px;font-size:34px;}

  .tagline{
    position:absolute;left:33px;top:428px;margin:0;
    font-size:16px;color:var(--tagline);letter-spacing:.01em;
  }

  .contact{position:absolute;left:573px;top:216px;}
  .contact__name{
    margin:0;font-family:"Jost",Arial,sans-serif;font-weight:600;
    font-size:27px;line-height:1;color:var(--ink);
  }
  .contact__name .first{color:var(--brand-red);}
  .contact__role{margin:3px 0 0 2px;font-size:13px;color:var(--text-body);}
  .contact__list{list-style:none;margin:22px 0 0;padding:0;}
  .contact__list li{
    display:flex;align-items:center;height:27px;
    font-size:18px;color:var(--text-body);
  }
  .contact__list li.gap{margin-top:25px;}
  .contact__list svg{width:16px;height:16px;margin:0 20px 0 2px;}
  .icon-fill{fill:var(--ink);}
  .icon-line{fill:none;stroke:var(--ink);stroke-width:1.5;stroke-linejoin:round;stroke-linecap:round;}
</style>
</head>
<body>

<section class="card card--front">
  <svg class="card__backdrop" viewBox="0 0 869 483" preserveAspectRatio="none" role="img" aria-label="Soft blue abstract wave artwork">
    <defs>
      <linearGradient id="frontBlue" x1="0" y1="0" x2="1" y2="0">
        <stop offset="0" stop-color="#86bde0"/><stop offset="1" stop-color="#2f7fb8"/>
      </linearGradient>
    </defs>
    <path fill="url(#frontBlue)" d="M258 0 C330 150 420 260 470 350 C495 400 510 450 515 483 L869 483 L869 0Z"/>
  </svg>

  <h1 class="brand__name">Clearpath Technology</h1>
  <p class="tagline">IT SERVICES, SOLUTIONS AND SUPPORT</p>
</section>

<section class="card card--back">
  <svg class="card__backdrop" viewBox="0 0 869 478" preserveAspectRatio="none" role="img" aria-label="Soft blue abstract wave artwork">
    <defs>
      <linearGradient id="backBlue" x1="0" y1="0" x2="1" y2="0">
        <stop offset="0" stop-color="#86bde0"/><stop offset="1" stop-color="#1a5e92"/>
      </linearGradient>
    </defs>
    <path fill="url(#backBlue)" d="M0 0 L125 0 C165 160 380 360 530 478 L0 478Z"/>
  </svg>

  <h2 class="brand__name">Clearpath Technology</h2>

  <div class="contact">
    <p class="contact__name"><span class="first">Marcus</span> Hale</p>
    <p class="contact__role">General Manager</p>
    <ul class="contact__list">
      <li><svg viewBox="0 0 16 16" aria-hidden="true"><path class="icon-fill" d="M1 5c0-2 3-3 7-3s7 1 7 3v1h-4V5H5v1H1z"/><path class="icon-fill" d="M4 7h8l2 6H2z"/></svg>07 3555 0148</li>
      <li><svg viewBox="0 0 16 16" aria-hidden="true"><path class="icon-fill" d="M4 0h8a1 1 0 011 1v14a1 1 0 01-1 1H4a1 1 0 01-1-1V1a1 1 0 011-1zm1 2v10h6V2zm3 11a1 1 0 100 2 1 1 0 000-2z"/></svg>0400 555 217</li>
      <li class="gap"><svg viewBox="0 0 16 16" aria-hidden="true"><rect class="icon-line" x="1.5" y="3.5" width="13" height="9"/><path class="icon-line" d="M1.5 3.5L8 9l6.5-5.5M1.5 12.5l5-4.5M14.5 12.5l-5-4.5"/></svg>mhale@clearpathit.com.au</li>
      <li><svg viewBox="0 0 16 16" aria-hidden="true"><path class="icon-line" d="M6.5 9.5l3-3M7 4l2-2a2.8 2.8 0 014 4l-2 2M9 12l-2 2a2.8 2.8 0 01-4-4l2-2"/></svg>www.clearpathit.com.au</li>
    </ul>
  </div>
</section>

</body>
</html>
```